Website redesign for Root and Renew

We would like to update the design of our current website to a more concise, conversion optimized design.
The goal of our website is to get our message across as concisely as possible plus encourage people to contact us for more information or to book a consultation.
We need a redesign of the home page and 1 internal page - just for design/layout purposes/format purposes.

Target Market(s)

Males 20-45 years old who are concerned about hair loss and who want to regrow their own hair.

Industry/Entity Type

Health And Wellness

Number of Pages Required

2 page

Font styles to use
Sans Serif

Colors
00a990
33a6d7
ffffff
9d9d9d

Requirements
Must have
• We want the home page to be very concise and to the point in getting the message across. We want to get across the following 6 key messages:
• 1. Dr Brambury story – why he created this solution
• 2. Hair loss is caused by a chemical imbalance
• 3. Root and renew conducts genetic and DNA analysis, then rebalances body chemistry, thus reversing the hair loss process and enabling your own hair to regrow naturally
• 4. Money back guaranteed results
• 5. Purely The Core ingredients – no harsh preservatives or chemicals are included
• 6. All ingredients are FDA approved and safe – no side effects
• We also need a strong call to action. We want people to call or email us to find out more information or to schedule a consultation.
• Here is our current website which is not performing as we would hope: http://www.rootandrenewhq.com/
• Here is our press release for further information: https://www.pressflarex.com/news/finally-we-now-have-a-cure-for-male-pattern-baldness-40528316
• I uploaded the logo files, but let me know if anything else is needed and I can add it.

```html
<!DOCTYPE html>
<html lang="en">
<head>
<meta charset="utf-8">
<title>Root and Renew – Hair Recovery Clinic</title>
<link rel="stylesheet" href="https://fonts.googleapis.com/css2?family=Alegreya+Sans:ital,wght@0,400;0,700;0,800;1,400&family=Open+Sans:ital,wght@0,400;0,600;0,700;1,400&display=swap">
<style>
:root{
  --teal:#4cc3cf;
  --teal-band:#5ccbd6;
  --green:#00a990;
  --blue:#33a6d7;
  --ink:#222629;
  --text:#3a3f44;
  --muted:#9d9d9d;
  --line:#e6e8ea;
  --soft:#f3f4f5;
  --footer:#1f2326;
  --footer-bottom:#181b1d;
  --white:#ffffff;
}
*{box-sizing:border-box;margin:0;padding:0}
html,body{width:1200px;height:3944px;overflow:hidden}
body{font-family:"Open Sans",Arial,sans-serif;color:var(--text);background:var(--white);font-size:15px;line-height:1.6}
h1,h2,h3,h4{font-family:"Alegreya Sans","Trebuchet MS",sans-serif;color:var(--ink);font-weight:800;line-height:1.2}

/* header */
.site-header{height:72px;display:flex;align-items:center;justify-content:space-between;padding:0 70px;border-bottom:1px solid var(--line)}
.brand{display:flex;align-items:center;gap:10px}
.brand-dot{width:22px;height:22px;border-radius:50%;background:var(--green)}
.brand-text{display:flex;flex-direction:column;line-height:1.05}
.brand-name{font-family:"Alegreya Sans",sans-serif;font-weight:700;font-size:24px;color:#4a5358}
.brand-by{font-size:12px;color:var(--green)}
.main-nav{display:flex;align-items:center;gap:34px;font-size:14px;color:#4a5358}
.main-nav .active{color:var(--green);border-bottom:2px solid var(--green);padding-bottom:3px}
.main-nav .has-sub::after{content:" ▾";font-size:10px}

/* hero */
.hero{height:520px;position:relative;background:linear-gradient(90deg,#d8dde1 0%,#eef1f3 40%,#f8f9fa 60%,#ffffff 100%);overflow:hidden}
.hero-photo{position:absolute;left:0;top:0;width:580px;height:100%;background:linear-gradient(100deg,#aeb6bc 0%,#c9d0d5 55%,rgba(238,241,243,0) 100%)}
.hero-copy{position:absolute;left:600px;top:86px;width:540px}
.hero-copy h1{font-size:42px;text-align:right}
.hero-copy p{font-size:13px;color:#707a80;margin-top:18px;text-align:right;line-height:1.6}
.hero-phone{display:flex;align-items:center;justify-content:flex-end;gap:18px;margin-top:34px;font-family:"Alegreya Sans",sans-serif;font-weight:700;font-size:50px;color:var(--ink);line-height:1}
.slider-dots{position:absolute;left:540px;bottom:30px;display:flex;gap:14px}
.slider-dots span{width:12px;height:12px;border-radius:50%;background:var(--ink)}
.slider-dots span.on{background:var(--white)}

/* intro */
.intro{height:328px;text-align:center;padding-top:62px;border-bottom:1px solid var(--line);width:1040px;margin:0 auto}
.intro h2{font-size:44px}
.lead{font-family:"Alegreya Sans",sans-serif;font-size:27px;color:var(--teal);margin-top:40px;line-height:1.2}
.intro .small{font-size:14px;color:var(--muted);width:780px;margin:14px auto 0;line-height:1.55}

/* services */
.services{height:600px;text-align:center;padding-top:72px;border-bottom:1px solid var(--line);width:1040px;margin:0 auto}
.services h2{font-size:44px;width:760px;margin:0 auto}
.service-grid{display:grid;grid-template-columns:repeat(4,240px);gap:26px;justify-content:center;margin-top:40px}
.service-photo{height:170px}
.service-grid h3{font-family:"Alegreya Sans",sans-serif;font-weight:400;color:var(--teal);font-size:24px;margin-top:22px;line-height:1.15}
.btn{display:inline-block;font-family:"Open Sans",sans-serif;font-weight:700;font-size:13px;border-radius:22px;padding:11px 28px;line-height:1.4}
.btn-teal{background:var(--teal);color:var(--white);margin-top:36px}
.btn-dark{background:var(--ink);color:var(--white)}

/* consultation */
.consult{height:520px;margin-top:40px;background:var(--soft);position:relative}
.consult-photo{position:absolute;right:0;top:0;width:440px;height:100%;background:linear-gradient(90deg,rgba(243,244,245,0) 0%,#d7dbdf 30%,#c3c9ce 100%)}
.consult-copy{position:absolute;left:80px;top:80px;width:620px}
.consult-copy h2{font-size:44px}
.consult-copy p{font-style:italic;color:var(--teal);font-size:18px;margin-top:32px;line-height:1.6}
.consult-copy .btn{margin-top:46px}

/* why */
.why{height:520px;text-align:center;padding-top:76px;border-bottom:1px solid var(--line);width:1040px;margin:0 auto}
.why h2{font-size:44px}
.why-grid{display:grid;grid-template-columns:repeat(3,320px);gap:40px;justify-content:center;margin-top:36px}
.why-photo{height:220px}
.why-grid h3{font-family:"Alegreya Sans",sans-serif;font-weight:400;color:var(--teal);font-size:24px;margin-top:22px}
.why-grid p{font-size:13px;color:var(--muted);margin-top:8px;line-height:1.55}

/* testimonials */
.reviews{height:672px;text-align:center;padding-top:62px}
.reviews h2{font-size:44px}
.review-grid{display:grid;grid-template-columns:repeat(3,300px);gap:70px;justify-content:center;margin-top:46px}
.quote-mark{font-family:Georgia,serif;font-size:60px;line-height:1;color:var(--green)}
.avatar{width:84px;height:84px;border-radius:50%;margin:10px auto 0;background:radial-gradient(circle at 50% 40%,#c9ced3,#8f979d)}
.review-grid blockquote{font-size:13px;color:var(--muted);margin-top:30px;line-height:1.6}
.review-grid cite{display:block;font-style:normal;font-weight:700;color:var(--ink);font-size:15px;margin-top:22px}

/* cta band */
.cta-band{height:348px;background:var(--teal-band);text-align:center;padding-top:100px}
.cta-band h2{color:var(--white);font-size:44px}
.cta-band p{color:var(--white);font-style:italic;font-size:18px;width:700px;margin:20px auto 0;line-height:1.55}
.cta-band .btn{margin-top:28px}

/* footer */
.site-footer{height:324px;background:var(--footer);color:#9aa1a6;position:relative}
.footer-cols{display:grid;grid-template-columns:repeat(3,1fr);gap:60px;padding:46px 80px 0}
.footer-cols h4{font-family:"Open Sans",sans-serif;color:var(--white);font-size:16px;font-weight:700;margin-bottom:16px}
.footer-cols p,.footer-cols li{font-size:13px;line-height:1.7;list-style:none}
.footer-cols li{display:flex;align-items:center;gap:10px}
.footer-cols li svg{flex:none}
.footer-bottom{position:absolute;left:0;right:0;bottom:0;height:70px;background:var(--footer-bottom);display:flex;align-items:center;justify-content:space-between;padding:0 80px;font-size:12px}
.footer-bottom .accent{color:var(--green)}
.social{display:flex;gap:16px}
.social span{width:14px;height:14px;border-radius:50%;background:#6d757a}
</style>
</head>
<body>

<header class="site-header">
  <div class="brand">
    <span class="brand-dot"></span>
    <div class="brand-text">
      <span class="brand-name">Root &amp; Renew</span>
      <span class="brand-by">by Alan Brambury M.D.</span>
    </div>
  </div>
  <nav class="main-nav">
    <span class="active has-sub">Home</span>
    <span>About us</span>
    <span class="has-sub">Services</span>
    <span class="has-sub">News</span>
    <span>Contacts</span>
    <span class="has-sub">Pages</span>
    <svg width="16" height="16" viewBox="0 0 16 16" aria-label="Search"><circle cx="6.5" cy="6.5" r="5" fill="none" stroke="#4a5358" stroke-width="2"/><line x1="10.5" y1="10.5" x2="15" y2="15" stroke="#4a5358" stroke-width="2"/></svg>
  </nav>
</header>

<section class="hero">
  <div class="hero-photo" role="img" aria-label="Smiling young man touching his full head of hair"></div>
  <div class="hero-copy">
    <h1>If you suffer from a hair loss or balding, it's good news for you!</h1>
    <p>Dr Brambury lost his own hair at 28 and spent years finding a way to regrow it naturally. Now he shares that solution with you. Call us for details.</p>
    <div class="hero-phone">
      <svg width="40" height="40" viewBox="0 0 24 24" aria-hidden="true"><path fill="#00a990" d="M6.6 10.8a15.2 15.2 0 0 0 6.6 6.6l2.2-2.2a1 1 0 0 1 1-.25 11.4 11.4 0 0 0 3.6.57 1 1 0 0 1 1 1V20a1 1 0 0 1-1 1A17 17 0 0 1 3 4a1 1 0 0 1 1-1h3.5a1 1 0 0 1 1 1c0 1.25.2 2.45.57 3.57a1 1 0 0 1-.25 1z"/></svg>
      555–284–7710
    </div>
  </div>
  <div class="slider-dots"><span></span><span class="on"></span><span></span></div>
</section>

<section class="intro">
  <h2>It's not about hair loss, it's about hair recovery...</h2>
  <p class="lead">Our clinic has always been about high-quality hair recovery!</p>
  <p class="small">Hair loss is caused by a chemical imbalance. We run genetic and DNA analysis, then rebalance your body chemistry so your own hair can regrow naturally.</p>
</section>

<section class="services">
  <h2>See the full list of our Hair recovery &amp; Hair loss prevention services:</h2>
  <div class="service-grid">
    <article>
      <div class="service-photo" role="img" aria-label="Close-up of a thinning scalp receiving laser treatment" style="background:linear-gradient(160deg,#e9dcd2,#c7b0a2)"></div>
      <h3>Laser Hair Regrowth</h3>
    </article>
    <article>
      <div class="service-photo" role="img" aria-label="Top view of a balding crown" style="background:linear-gradient(160deg,#caa58a,#7a5846)"></div>
      <h3>Follicular Regen Treatment</h3>
    </article>
    <article>
      <div class="service-photo" role="img" aria-label="Specialist fitting a hair system" style="background:linear-gradient(160deg,#d9d3cc,#8e8276)"></div>
      <h3>Non-Surgical Hair Replacement</h3>
    </article>
    <article>
      <div class="service-photo" role="img" aria-label="Surgeon performing a hair transplant" style="background:linear-gradient(160deg,#e4d6cb,#a98e7c)"></div>
      <h3>Surgical Hair Replacement</h3>
    </article>
  </div>
  <span class="btn btn-teal">See all Services</span>
</section>

<section class="consult">
  <div class="consult-photo" role="img" aria-label="Friendly doctor in a white coat"></div>
  <div class="consult-copy">
    <h2>Looking for consultation or hair care assistance?</h2>
    <p>Fill out our registration form or contact us today to book an appointment with our first-class specialists who will help you find out and eliminate any hair problems you may have</p>
    <span class="btn btn-dark">Make an Appointment</span>
  </div>
</section>

<section class="why">
  <h2>Why our Hair Recovery Clinic is the best?</h2>
  <div class="why-grid">
    <article>
      <div class="why-photo" role="img" aria-label="Man styling thick dark hair" style="background:linear-gradient(160deg,#cfc6bf,#3f3733)"></div>
      <h3>Range of Choices</h3>
      <p>Every plan comes with money back guaranteed results, so you can choose the treatment that suits you without risk.</p>
    </article>
    <article>
      <div class="why-photo" role="img" aria-label="Team of clinic doctors and nurses" style="background:linear-gradient(160deg,#eef2f4,#b9c6ce)"></div>
      <h3>Experienced Staff</h3>
      <p>Our specialists use Purely The Core ingredients only, with no harsh preservatives or chemicals included.</p>
    </article>
    <article>
      <div class="why-photo" role="img" aria-label="Gloved hands holding a syringe" style="background:linear-gradient(160deg,#e6eef2,#9fb8c6)"></div>
      <h3>Top Medication &amp; Equipment</h3>
      <p>All ingredients we use are FDA approved and safe, with no side effects, backed by modern equipment.</p>
    </article>
  </div>
</section>

<section class="reviews">
  <h2>See what our Happy Patients say</h2>
  <div class="review-grid">
    <figure>
      <div class="quote-mark">“</div>
      <div class="avatar" role="img" aria-label="Portrait of patient Martin Caldwell"></div>
      <blockquote>I've always been afraid of going bald, and for a few years it really got to me. Thankfully, starting treatment here changed all that, and now I feel confident again, thanks to this team!</blockquote>
      <cite>Martin Caldwell</cite>
    </figure>
    <figure>
      <div class="quote-mark">“</div>
      <div class="avatar" role="img" aria-label="Portrait of patient Owen Fairley"></div>
      <blockquote>Since the start of my balding process I tried every remedy out there. A friend recommended this clinic, I signed up for the treatment, and after five months my hair is thick again.</blockquote>
      <cite>Owen Fairley</cite>
    </figure>
    <figure>
      <div class="quote-mark">“</div>
      <div class="avatar" role="img" aria-label="Portrait of patient Simon Ashdown"></div>
      <blockquote>It's true that men do not take balding lightly. For me this was a hard time, as I lost my self-esteem too. The doctors here helped me feel like myself once more.</blockquote>
      <cite>Simon Ashdown</cite>
    </figure>
  </div>
</section>

<section class="cta-band">
  <h2>Do you suffer from balding or want to prevent it timely?</h2>
  <p>Get in touch with our clinic today, to avoid feeling bad about your hair's health and looks tomorrow!</p>
  <span class="btn btn-dark">Book an Appointment</span>
</section>

<footer class="site-footer">
  <div class="footer-cols">
    <div>
      <h4>About us</h4>
      <p>Root &amp; Renew analyses your DNA and rebalances body chemistry to help you regrow your own hair, naturally and safely.</p>
    </div>
    <div>
      <h4>Contact info</h4>
      <ul>
        <li><svg width="12" height="12" viewBox="0 0 24 24"><path fill="#00a990" d="M6.6 10.8a15.2 15.2 0 0 0 6.6 6.6l2.2-2.2a1 1 0 0 1 1-.25 11.4 11.4 0 0 0 3.6.57 1 1 0 0 1 1 1V20a1 1 0 0 1-1 1A17 17 0 0 1 3 4a1 1 0 0 1 1-1h3.5a1 1 0 0 1 1 1c0 1.25.2 2.45.57 3.57a1 1 0 0 1-.25 1z"/></svg>555-284-7710</li>
        <li><svg width="12" height="12" viewBox="0 0 24 24"><rect x="2" y="5" width="20" height="14" fill="none" stroke="#00a990" stroke-width="2"/><path d="M2 6l10 7 10-7" fill="none" stroke="#00a990" stroke-width="2"/></svg>info@rootandrenewhq.com</li>
        <li><svg width="12" height="12" viewBox="0 0 24 24"><path fill="#00a990" d="M12 2a7 7 0 0 0-7 7c0 5 7 13 7 13s7-8 7-13a7 7 0 0 0-7-7zm0 9.5A2.5 2.5 0 1 1 12 6.5a2.5 2.5 0 0 1 0 5z"/></svg>120 Linden Avenue, Suite 4</li>
      </ul>
    </div>
    <div>
      <h4>Opening hours</h4>
      <ul>
        <li>Monday - Friday: 9am - 6pm</li>
        <li>Saturday: 10am - 4pm</li>
        <li>Sunday: closed</li>
      </ul>
    </div>
  </div>
  <div class="footer-bottom">
    <span>© 2024 <span class="accent">Root &amp; Renew</span>. Privacy Policy</span>
    <div class="social"><span></span><span></span><span></span><span></span><span></span></div>
  </div>
</footer>

</body>
</html>
```